I WAS JUST GIVING A SIZE THAT THE LABEL NEEDS TO BE ON OUR PACKAGING BAGS, IT IS 4X6. PLEASE MAKE SURE THAT DESIGN WILL FIT ON THAT SIZE.

We are looking to have you design the packaging for our coffee that will be sold online. The basics that we want on all the different varieties is our company name "Halvorsen's Gourmet Coffee & tagline " Gourmet Coffee for the Everyday Coffee Lover" and logo which is attached. If you ffind a different logo and want to change the colors in the logo, we are open to any suggestions. Our thoughts are travel the world with your coffee, that why we went with compass star. We are looking to use black bags for all as well. We would like a different picture background that is relatable to the type of coffee, if possible. The colors need to pop on the black bag. We need designs for the following flavors of coffee...

Brazilian Dark Roast
Columbian Supremo
100% Columbian Dark Roast
French Vanilla
Velvet Meadow
Kona Blend
Jamaican Blue Mountain Blend
Sumatra
Hazelnut
Irish Cream
Hawaiian Macadamia Nut Blend
Amaretto

All these flavors will be sold in 5# and 2# packages

```html
<!DOCTYPE html>
<html lang="en">
<head>
<meta charset="utf-8">
<title>Halvorsen's Gourmet Coffee – Packaging Range</title>
<link rel="stylesheet" href="https://fonts.googleapis.com/css2?family=Cormorant+Garamond:wght@500;600&family=Roboto:wght@400&family=Roboto+Condensed:wght@400&display=swap">
<style>
  :root {
    --canvas: #ffffff;
    --ink: #111111;
    --bag-top: #2e2e2e;
    --bag-mid: #232323;
    --bag-bottom: #1b1b1b;
    --bag-text: #e9e9e9;
    --bag-muted: #8d8d8d;
    --logo-panel: #000000;
    --green: #0f9a47;
    --forest: #0e4a24;
    --teal: #138275;
    --yellow: #d2c21a;
    --orange: #e38112;
    --red: #d8291f;
    --dark-brown: #5b3519;
    --brown: #7c4624;
    --gold: #a07528;
    --blue: #1688c4;
    --plum: #97236f;
    --mauve: #a9888e;
  }
  * { box-sizing: border-box; margin: 0; padding: 0; }
  html, body { width: 1200px; height: 900px; overflow: hidden; background: var(--canvas); }
  .board { position: relative; width: 1200px; height: 900px; font-family: "Roboto", Arial, sans-serif; color: var(--ink); }

  .board-title { position: absolute; left: 477px; top: 76px; font-size: 18px; font-weight: 400; letter-spacing: .02em; }
  .section-label { position: absolute; font-size: 19px; letter-spacing: .01em; }
  .section-label.colors { left: 728px; top: 658px; }
  .section-label.range { left: 28px; top: 716px; }

  .logo-panel {
    position: absolute; left: 829px; top: 28px; width: 334px; height: 159px;
    background: var(--logo-panel); display: flex; flex-direction: column; align-items: center; justify-content: center;
  }

  .wordmark { font-family: "Cormorant Garamond", Georgia, serif; font-weight: 600; color: var(--bag-text); text-align: center; line-height: 1; text-transform: uppercase; }
  .wordmark .line-name { display: block; font-size: 2.6em; letter-spacing: .02em; }
  .wordmark .line-sub { display: block; font-size: 1.55em; letter-spacing: .12em; margin-top: .15em; }
  .mark-dot { display: block; width: 4.6em; height: 4.6em; border: .25em solid var(--bag-text); border-radius: 50%; margin: 0 auto .9em; }
  .logo-panel .wordmark { font-size: 10px; }

  .swatches { position: absolute; left: 728px; top: 688px; display: flex; }
  .swatches span { width: 36.25px; height: 38px; display: block; }

  /* Flat bag label; every position is in bag em, text sizes live on inner spans */
  .bag {
    position: absolute; width: 37em; height: 65.8em; --accent: var(--green);
    background: linear-gradient(180deg, var(--bag-top) 0%, var(--bag-mid) 45%, var(--bag-bottom) 100%);
    color: var(--bag-text); overflow: hidden; box-shadow: 0 0 0 1px rgba(0,0,0,.35);
  }
  .bag .zip { position: absolute; left: 0; right: 0; top: 5.3em; height: .15em; background: #111; }
  .bag .valve { position: absolute; left: 50%; top: 11.2em; width: 2.1em; height: 2.1em; margin-left: -1.05em; border-radius: 50%; border: .2em solid #141414; background: #262626; }
  .bag .brand { position: absolute; left: 0; right: 0; top: 16em; }
  .bag .flavor-band {
    position: absolute; left: 0; right: 0; top: 37.4em; height: 4.4em;
    background: linear-gradient(180deg, transparent 0 .25em, var(--accent) .25em .45em, transparent .45em .75em, var(--accent) .75em calc(100% - .75em), transparent calc(100% - .75em) calc(100% - .45em), var(--accent) calc(100% - .45em) calc(100% - .25em), transparent calc(100% - .25em));
    display: flex; align-items: center; justify-content: center;
  }
  .bag .flavor-name { font-family: "Cormorant Garamond", Georgia, serif; font-weight: 600; font-variant: small-caps; font-size: 1.65em; letter-spacing: .05em; color: var(--bag-text); white-space: nowrap; }
  .bag .copy { position: absolute; left: 7.3em; right: 5em; top: 42.8em; font-family: "Cormorant Garamond", Georgia, serif; color: var(--bag-muted); text-align: justify; }
  .bag .copy .lead { font-size: 1.1em; font-variant: small-caps; line-height: 1.05; }
  .bag .copy .fine { font-size: .6em; font-variant: small-caps; line-height: 1.2; margin-top: .6em; }
  .bag .copy .faint { font-size: .62em; line-height: 1.35; margin: 1em 9% 0; text-align: center; opacity: .55; }
  .bag .rule { position: absolute; left: 0; right: 0; height: .12em; background: var(--accent); }
  .bag .rule.one { top: 56.6em; }
  .bag .rule.two { top: 57.4em; }
  .bag .weight { position: absolute; left: 0; right: 0; top: 59.3em; text-align: center; line-height: 1; }
  .bag .weight span { font-family: "Roboto Condensed", Arial, sans-serif; font-size: 1.15em; color: #cfcfcf; }
  .bag .site { position: absolute; left: 0; right: 0; top: 62.3em; text-align: center; line-height: 1; }
  .bag .site span { font-family: "Cormorant Garamond", Georgia, serif; font-size: .95em; color: #555; }

  .bag.hero { left: 48px; top: 32px; font-size: 10px; }
  .bag.shelf { top: 237px; font-size: 5.85px; }
  .bag.thumb { top: 748px; font-size: 2.1px; }
</style>
</head>
<body>
<main class="board">

  <h1 class="board-title">HALVORSEN'S GOURMET COFFEE</h1>

  <div class="logo-panel">
    <div class="wordmark"><span class="mark-dot"></span><span class="line-name">Halvorsen's</span><span class="line-sub">Gourmet</span><span class="line-sub">Coffee</span></div>
  </div>

  <article class="bag hero" style="--accent: var(--green);">
    <div class="zip"></div><div class="valve"></div>
    <div class="brand wordmark"><span class="mark-dot"></span><span class="line-name">Halvorsen's</span><span class="line-sub">Gourmet</span><span class="line-sub">Coffee</span></div>
    <div class="flavor-band"><span class="flavor-name">Brasilian Dark Roast</span></div>
    <div class="copy">
      <p class="lead">Lorem ipsum dolor sit amet, consectetur adipiscing elit. Quisque ipsum felis, feugiat sit</p>
      <p class="fine">Lorem ipsum dolor sit amet, consectetur adipiscing elit. Quisque ipsum felis, feugiat sit amet est vel condimentum vestibulum quam. Proin commodo, purus in vehicula hendrerit, ante odio varius justo, pretium</p>
      <p class="faint">lorem ipsum dolor sit amet, consectetur adipiscing elit, quisque ipsum felis, feugiat sit amet est vel condimentum vestibulum quam proin commodo purus in vehicula hendrerit, ante odio varius justo, pretium convallis neque nulla ut arcu, nullam elementum est</p>
    </div>
    <div class="rule one"></div><div class="rule two"></div>
    <p class="weight"><span>netto weight 5 oz</span></p>
    <p class="site"><span>www.halvorsensgourmetcoffee.com</span></p>
  </article>

  <article class="bag shelf" style="left:473px; --accent: var(--gold);">
    <div class="zip"></div><div class="valve"></div>
    <div class="brand wordmark"><span class="mark-dot"></span><span class="line-name">Halvorsen's</span><span class="line-sub">Gourmet</span><span class="line-sub">Coffee</span></div>
    <div class="flavor-band"><span class="flavor-name">Columbian Supremo</span></div>
    <div class="copy">
      <p class="lead">Lorem ipsum dolor sit amet, consectetur adipiscing elit. Quisque ipsum felis, feugiat sit</p>
      <p class="fine">Lorem ipsum dolor sit amet, consectetur adipiscing elit. Quisque ipsum felis, feugiat sit amet est vel condimentum vestibulum quam. Proin commodo, purus in vehicula hendrerit, ante odio varius justo, pretium</p>
      <p class="faint">lorem ipsum dolor sit amet, consectetur adipiscing elit, quisque ipsum felis, feugiat sit amet est vel condimentum vestibulum quam proin commodo purus in vehicula hendrerit, ante odio varius justo, pretium convallis neque nulla ut arcu, nullam elementum est</p>
    </div>
    <div class="rule one"></div><div class="rule two"></div>
    <p class="weight"><span>netto weight 5 oz</span></p>
    <p class="site"><span>www.halvorsensgourmetcoffee.com</span></p>
  </article>

  <article class="bag shelf" style="left:675px; --accent: var(--teal);">
    <div class="zip"></div><div class="valve"></div>
    <div class="brand wordmark"><span class="mark-dot"></span><span class="line-name">Halvorsen's</span><span class="line-sub">Gourmet</span><span class="line-sub">Coffee</span></div>
    <div class="flavor-band"><span class="flavor-name">Kona Blend</span></div>
    <div class="copy">
      <p class="lead">Lorem ipsum dolor sit amet, consectetur adipiscing elit. Quisque ipsum felis, feugiat sit</p>
      <p class="fine">Lorem ipsum dolor sit amet, consectetur adipiscing elit. Quisque ipsum felis, feugiat sit amet est vel condimentum vestibulum quam. Proin commodo, purus in vehicula hendrerit, ante odio varius justo, pretium</p>
      <p class="faint">lorem ipsum dolor sit amet, consectetur adipiscing elit, quisque ipsum felis, feugiat sit amet est vel condimentum vestibulum quam proin commodo purus in vehicula hendrerit, ante odio varius justo, pretium convallis neque nulla ut arcu, nullam elementum est</p>
    </div>
    <div class="rule one"></div><div class="rule two"></div>
    <p class="weight"><span>netto weight 5 oz</span></p>
    <p class="site"><span>www.halvorsensgourmetcoffee.com</span></p>
  </article>

  <article class="bag shelf" style="left:880px; --accent: var(--red);">
    <div class="zip"></div><div class="valve"></div>
    <div class="brand wordmark"><span class="mark-dot"></span><span class="line-name">Halvorsen's</span><span class="line-sub">Gourmet</span><span class="line-sub">Coffee</span></div>
    <div class="flavor-band"><span class="flavor-name">Amaretto</span></div>
    <div class="copy">
      <p class="lead">Lorem ipsum dolor sit amet, consectetur adipiscing elit. Quisque ipsum felis, feugiat sit</p>
      <p class="fine">Lorem ipsum dolor sit amet, consectetur adipiscing elit. Quisque ipsum felis, feugiat sit amet est vel condimentum vestibulum quam. Proin commodo, purus in vehicula hendrerit, ante odio varius justo, pretium</p>
      <p class="faint">lorem ipsum dolor sit amet, consectetur adipiscing elit, quisque ipsum felis, feugiat sit amet est vel condimentum vestibulum quam proin commodo purus in vehicula hendrerit, ante odio varius justo, pretium convallis neque nulla ut arcu, nullam elementum est</p>
    </div>
    <div class="rule one"></div><div class="rule two"></div>
    <p class="weight"><span>netto weight 5 oz</span></p>
    <p class="site"><span>www.halvorsensgourmetcoffee.com</span></p>
  </article>

  <p class="section-label colors">COLOR RANGE</p>
  <div class="swatches" aria-label="Colour range">
    <span style="background:var(--green)"></span><span style="background:var(--forest)"></span><span style="background:var(--teal)"></span><span style="background:var(--yellow)"></span><span style="background:var(--orange)"></span><span style="background:var(--red)"></span><span style="background:var(--dark-brown)"></span><span style="background:var(--brown)"></span><span style="background:var(--gold)"></span><span style="background:var(--blue)"></span><span style="background:var(--plum)"></span><span style="background:var(--mauve)"></span>
  </div>

  <p class="section-label range">FULL RANGE</p>

  <article class="bag thumb" style="left:25px; --accent: var(--orange);"><div class="zip"></div><div class="valve"></div><div class="brand wordmark"><span class="mark-dot"></span><span class="line-name">Halvorsen's</span><span class="line-sub">Gourmet</span><span class="line-sub">Coffee</span></div><div class="flavor-band"><span class="flavor-name">French Vanilla</span></div><div class="rule one"></div><div class="rule two"></div><p class="weight"><span>netto weight 5 oz</span></p></article>
  <article class="bag thumb" style="left:123px; --accent: var(--brown);"><div class="zip"></div><div class="valve"></div><div class="brand wordmark"><span class="mark-dot"></span><span class="line-name">Halvorsen's</span><span class="line-sub">Gourmet</span><span class="line-sub">Coffee</span></div><div class="flavor-band"><span class="flavor-name">Sumatra</span></div><div class="rule one"></div><div class="rule two"></div><p class="weight"><span>netto weight 5 oz</span></p></article>
  <article class="bag thumb" style="left:221px; --accent: var(--dark-brown);"><div class="zip"></div><div class="valve"></div><div class="brand wordmark"><span class="mark-dot"></span><span class="line-name">Halvorsen's</span><span class="line-sub">Gourmet</span><span class="line-sub">Coffee</span></div><div class="flavor-band"><span class="flavor-name">Colombian Dark Roast</span></div><div class="rule one"></div><div class="rule two"></div><p class="weight"><span>netto weight 5 oz</span></p></article>
  <article class="bag thumb" style="left:319px; --accent: var(--blue);"><div class="zip"></div><div class="valve"></div><div class="brand wordmark"><span class="mark-dot"></span><span class="line-name">Halvorsen's</span><span class="line-sub">Gourmet</span><span class="line-sub">Coffee</span></div><div class="flavor-band"><span class="flavor-name">Blue Mountain Blend</span></div><div class="rule one"></div><div class="rule two"></div><p class="weight"><span>netto weight 5 oz</span></p></article>
  <article class="bag thumb" style="left:417px; --accent: var(--plum);"><div class="zip"></div><div class="valve"></div><div class="brand wordmark"><span class="mark-dot"></span><span class="line-name">Halvorsen's</span><span class="line-sub">Gourmet</span><span class="line-sub">Coffee</span></div><div class="flavor-band"><span class="flavor-name">Hazelnut</span></div><div class="rule one"></div><div class="rule two"></div><p class="weight"><span>netto weight 5 oz</span></p></article>
  <article class="bag thumb" style="left:515px; --accent: var(--yellow);"><div class="zip"></div><div class="valve"></div><div class="brand wordmark"><span class="mark-dot"></span><span class="line-name">Halvorsen's</span><span class="line-sub">Gourmet</span><span class="line-sub">Coffee</span></div><div class="flavor-band"><span class="flavor-name">Velvet Meadow</span></div><div class="rule one"></div><div class="rule two"></div><p class="weight"><span>netto weight 5 oz</span></p></article>
  <article class="bag thumb" style="left:613px; --accent: var(--gold);"><div class="zip"></div><div class="valve"></div><div class="brand wordmark"><span class="mark-dot"></span><span class="line-name">Halvorsen's</span><span class="line-sub">Gourmet</span><span class="line-sub">Coffee</span></div><div class="flavor-band"><span class="flavor-name">Colombian Supremo</span></div><div class="rule one"></div><div class="rule two"></div><p class="weight"><span>netto weight 5 oz</span></p></article>
  <article class="bag thumb" style="left:711px; --accent: var(--green);"><div class="zip"></div><div class="valve"></div><div class="brand wordmark"><span class="mark-dot"></span><span class="line-name">Halvorsen's</span><span class="line-sub">Gourmet</span><span class="line-sub">Coffee</span></div><div class="flavor-band"><span class="flavor-name">Brazilian Dark Roast</span></div><div class="rule one"></div><div class="rule two"></div><p class="weight"><span>netto weight 5 oz</span></p></article>
  <article class="bag thumb" style="left:809px; --accent: var(--forest);"><div class="zip"></div><div class="valve"></div><div class="brand wordmark"><span class="mark-dot"></span><span class="line-name">Halvorsen's</span><span class="line-sub">Gourmet</span><span class="line-sub">Coffee</span></div><div class="flavor-band"><span class="flavor-name">Irish Cream</span></div><div class="rule one"></div><div class="rule two"></div><p class="weight"><span>netto weight 5 oz</span></p></article>
  <article class="bag thumb" style="left:907px; --accent: var(--mauve);"><div class="zip"></div><div class="valve"></div><div class="brand wordmark"><span class="mark-dot"></span><span class="line-name">Halvorsen's</span><span class="line-sub">Gourmet</span><span class="line-sub">Coffee</span></div><div class="flavor-band"><span class="flavor-name">Macadamia Nut Blend</span></div><div class="rule one"></div><div class="rule two"></div><p class="weight"><span>netto weight 5 oz</span></p></article>
  <article class="bag thumb" style="left:1005px; --accent: var(--teal);"><div class="zip"></div><div class="valve"></div><div class="brand wordmark"><span class="mark-dot"></span><span class="line-name">Halvorsen's</span><span class="line-sub">Gourmet</span><span class="line-sub">Coffee</span></div><div class="flavor-band"><span class="flavor-name">Kona Blend</span></div><div class="rule one"></div><div class="rule two"></div><p class="weight"><span>netto weight 5 oz</span></p></article>
  <article class="bag thumb" style="left:1103px; --accent: var(--red);"><div class="zip"></div><div class="valve"></div><div class="brand wordmark"><span class="mark-dot"></span><span class="line-name">Halvorsen's</span><span class="line-sub">Gourmet</span><span class="line-sub">Coffee</span></div><div class="flavor-band"><span class="flavor-name">Amaretto</span></div><div class="rule one"></div><div class="rule two"></div><p class="weight"><span>netto weight 5 oz</span></p></article>

</main>
</body>
</html>
```